Brackwell + Sorrent Architecture Ltd Stationary rebrand Lead designer to create a fresh clean modern...

We have recieved a great new logo design and now we are after a consistant fresh and modern stationary to match the new design. Business card design, Letter Head design, presentatnion folders and other stationery within the package. I have also added some of our existing layouts for presentation we would like updating with the new look, We would like a clean modern fresh design that looks visually pleasing on the page. we cant wait to see what you come up with!!!!

Target Market(s)

young professionals and middle age clients

Industry/Entity Type

Architect

Contact Information for Business Card

i have uploarded our orginal business card that has all the details attached.

Font styles to use
Sans Serif

Colors
000000
ffffff
d3d3d3

Requirements
Must have
• Logo and our contact information
Nice to have
• white sape around the card to give a clean look.

```html
<!DOCTYPE html>
<html lang="en">
<head>
<meta charset="utf-8">
<title>Brackwell + Sorrent Architecture — Stationery</title>
<link href="https://fonts.googleapis.com/css2?family=Lato:wght@400;700&display=swap" rel="stylesheet">
<style>
  :root{
    --black:#000000;
    --ink:#111111;
    --white:#ffffff;
    --light:#d3d3d3;
    --grey-text:#6f6f6f;
    --stage:#bcbdbf;
    --faint:#ececec;
  }
  *{box-sizing:border-box;margin:0;padding:0}
  html,body{width:1200px;height:1200px;overflow:hidden}
  body{background:var(--stage);font-family:'Lato',sans-serif;color:var(--ink);position:relative}
  .piece{position:absolute;background:var(--white);overflow:hidden}
  .texture{position:absolute;background:linear-gradient(135deg,rgba(211,211,211,.35),rgba(211,211,211,.08))}

  /* wordmark */
  .mark{display:flex;flex-direction:column;align-items:center;gap:3px;color:var(--ink);font-weight:700;text-align:center}
  .mark .sq{background:currentColor}
  .mark .name{letter-spacing:.08em;white-space:nowrap}
  .mark .sub{letter-spacing:.45em;white-space:nowrap;margin-right:-.45em}
  .mark.on-dark{color:var(--white)}

  /* letterhead */
  .letterhead{left:94px;top:70px;width:377px;height:533px}
  .letterhead .mark{position:absolute;left:23px;top:66px}
  .letterhead .mark .sq{width:12px;height:12px}
  .letterhead .mark .name{font-size:5.5px}
  .letterhead .mark .sub{font-size:3px}
  .lh-text{position:absolute;left:23px;width:330px;font-size:6px;line-height:10.2px;color:var(--grey-text);text-align:justify}
  .salute{top:155px;display:flex;justify-content:space-between;text-align:left}
  .sign-name{position:absolute;left:23px;top:314px;font-size:9px;color:#444}
  .sign-role{position:absolute;left:23px;top:325px;font-size:5.5px;color:var(--grey-text)}
  .signature{position:absolute;left:23px;top:337px;width:66px;height:24px;background:linear-gradient(90deg,#e2e2e2,#f2f2f2)}
  .lh-contact{position:absolute;left:23px;top:418px;font-size:5.2px;line-height:8.2px;color:var(--grey-text)}
  .lh-contact b{color:var(--ink)}

  /* envelope back */
  .env-back{left:509px;top:143px;width:498px;height:249px}
  .env-flap{position:absolute;left:0;top:0;width:100%;height:81px;background:var(--black);border-radius:0 0 12px 12px}
  .env-flap .mark{position:absolute;left:0;right:0;top:34px}
  .env-flap .mark .name{font-size:9px}
  .env-flap .mark .sub{font-size:4.5px}

  /* envelope front */
  .env-front{left:607px;top:288px;width:499px;height:248px}
  .env-front .bar{position:absolute;left:0;top:0;width:100%;height:4px;background:var(--black)}
  .env-front .mark{position:absolute;left:46px;top:52px}
  .env-front .mark .sq{width:22px;height:22px}
  .env-front .mark .name{font-size:9px}
  .env-front .mark .sub{font-size:4.8px}
  .env-contact{position:absolute;left:44px;top:135px;font-size:8px;line-height:11.5px;color:var(--grey-text)}
  .env-contact b{color:var(--ink)}
  .window{position:absolute;left:297px;top:127px;width:166px;height:78px;border-radius:16px;background:linear-gradient(110deg,#c9c9c9 0%,#d9d9d9 45%,#cfcfcf 46%,#bdbdbd 100%);border:1px solid #b5b5b5}

  /* folder */
  .folder-flap-left{position:absolute;left:159px;top:636px;width:58px;height:416px;background:#272526;clip-path:polygon(100% 0,0 12%,0 88%,100% 100%)}
  .folder-flap-bottom{position:absolute;left:217px;top:1052px;width:302px;height:132px;background:#272526;clip-path:polygon(0 0,100% 0,76% 100%,0 100%)}
  .folder-back{left:217px;top:636px;width:302px;height:416px;background:var(--black)}
  .folder-contact{position:absolute;left:32px;top:361px;font-size:4.4px;line-height:5.4px;color:var(--white)}
  .folder-front{left:520px;top:636px;width:303px;height:416px}
  .folder-front .mark{position:absolute;left:0;right:0;top:168px}
  .folder-front .mark .sq{width:30px;height:30px}
  .folder-front .mark .name{font-size:10.5px}
  .folder-front .mark .sub{font-size:5.5px}

  /* business cards */
  .card{width:187px}
  .card-back{left:809px;top:696px;height:107px;background:var(--black)}
  .card-back .mark{position:absolute;left:0;right:0;top:32px}
  .card-back .mark .sq{width:18px;height:18px}
  .card-back .mark .name{font-size:7px}
  .card-back .mark .sub{font-size:3.6px}
  .card-back .url{position:absolute;left:0;right:0;top:94px;text-align:center;font-size:4px;color:#bbb}
  .card-front{left:809px;top:816px;height:106px}
  .card-front .mark{position:absolute;left:16px;top:38px}
  .card-front .mark .sq{width:12px;height:12px}
  .card-front .mark .name{font-size:5px}
  .card-front .mark .sub{font-size:2.8px}
  .card-person{position:absolute;right:17px;top:33px;text-align:right}
  .card-person .who{font-size:6.5px;font-weight:700}
  .card-person .role{font-size:3.8px;color:var(--grey-text);margin-bottom:6px}
  .card-person ul{list-style:none;font-size:3.9px;line-height:6.2px;color:var(--grey-text)}
  .card-person li{display:flex;justify-content:flex-end;align-items:center;gap:2px}
  .card-person svg{width:4px;height:4px;fill:var(--ink)}
</style>
</head>
<body>

<!-- Letterhead -->
<section class="piece letterhead">
  <div class="texture" style="left:0;top:0;width:55px;height:61px" role="img" aria-label="Faint overlapping outline-rectangle pattern"></div>
  <div class="texture" style="left:230px;top:357px;width:147px;height:176px" role="img" aria-label="Faint overlapping outline-rectangle pattern"></div>
  <div class="mark"><span class="sq"></span><span class="name">BRACKWELL + SORRENT</span><span class="sub">ARCHITECTURE</span></div>
  <div class="lh-text salute"><span>Dear, Mr___________</span><span>Date : 14.06.2019</span></div>
  <p class="lh-text" style="top:181px">Lorem Ipsum is simply dummy text of the printing and typesetting industry. Lorem Ipsum has been the industry's standard dummy text ever since the1500s,when an unknown printer took a galley of type and scrambled it to make a type specimen book. It has survived not only five centuries, but also the leap into electronic typesetting, remaining essentially unchanged.</p>
  <p class="lh-text" style="top:231px">Lorem Ipsum is simply dummy text of the printing and typesetting industry. Lorem Ipsum has been the industry's standard dummy text ever since the1500s.</p>
  <p class="lh-text" style="top:262px">Lorem Ipsum is simply dummy text of the printing and typesetting industry.</p>
  <div class="sign-name">Your Name</div>
  <div class="sign-role">Designation</div>
  <div class="signature" role="img" aria-label="Handwritten signature"></div>
  <div class="lh-contact">
    <div><b>T :</b> 03 555 0142 &nbsp;&nbsp;<b>F :</b> 0274 555 019</div>
    <div><b>E :</b> daniel@bsarchitecture.co.nz</div>
    <div><b>W :</b> www.bsarchitecture.co.nz</div>
    <div><b>P :</b> PO Box 4180 Fairlie 7925</div>
    <div><b>A :</b> 18 Kelvin street Fairlie 7925</div>
  </div>
</section>

<!-- Envelope back -->
<section class="piece env-back">
  <div class="env-flap">
    <div class="mark on-dark"><span class="name">BRACKWELL + SORRENT</span><span class="sub">ARCHITECTURE</span></div>
  </div>
</section>

<!-- Envelope front -->
<section class="piece env-front">
  <div class="bar"></div>
  <div class="texture" style="left:0;top:4px;width:70px;height:65px" role="img" aria-label="Faint overlapping outline-rectangle pattern"></div>
  <div class="texture" style="left:312px;top:26px;width:187px;height:222px" role="img" aria-label="Faint overlapping outline-rectangle pattern"></div>
  <div class="mark"><span class="sq"></span><span class="name">BRACKWELL + SORRENT</span><span class="sub">ARCHITECTURE</span></div>
  <div class="env-contact">
    <div><b>T :</b> 03 555 0142</div>
    <div><b>F :</b> 0274 555 019</div>
    <div><b>E :</b> daniel@bsarchitecture.co.nz</div>
    <div><b>W :</b> www.bsarchitecture.co.nz</div>
    <div><b>P :</b> PO Box 4180 Fairlie 7925</div>
    <div><b>A :</b> 18 Kelvin street Fairlie 7925</div>
  </div>
  <div class="window"></div>
</section>

<!-- Presentation folder -->
<div class="folder-flap-left"></div>
<div class="folder-flap-bottom"></div>
<section class="piece folder-back">
  <div class="folder-contact">
    <div>T : 03 555 0142</div>
    <div>F : 0274 555 019</div>
    <div>E : daniel@bsarchitecture.co.nz</div>
    <div>W : www.bsarchitecture.co.nz</div>
    <div>P : PO Box 4180 Fairlie 7925</div>
    <div>A : 18 Kelvin street Fairlie 7925</div>
  </div>
</section>
<section class="piece folder-front">
  <div class="texture" style="left:0;top:0;width:45px;height:45px" role="img" aria-label="Faint overlapping outline-rectangle pattern"></div>
  <div class="texture" style="left:185px;top:278px;width:118px;height:138px" role="img" aria-label="Faint overlapping outline-rectangle pattern"></div>
  <div class="mark"><span class="sq"></span><span class="name">BRACKWELL + SORRENT</span><span class="sub">ARCHITECTURE</span></div>
</section>

<!-- Business cards -->
<section class="piece card card-back">
  <div class="mark on-dark"><span class="sq"></span><span class="name">BRACKWELL + SORRENT</span><span class="sub">ARCHITECTURE</span></div>
  <div class="url">www.bsarchitecture.co.nz</div>
</section>
<section class="piece card card-front">
  <div class="texture" style="left:0;top:0;width:30px;height:25px" role="img" aria-label="Faint overlapping outline-rectangle pattern"></div>
  <div class="texture" style="left:120px;top:60px;width:67px;height:46px" role="img" aria-label="Faint overlapping outline-rectangle pattern"></div>
  <div class="mark"><span class="sq"></span><span class="name">BRACKWELL + SORRENT</span><span class="sub">ARCHITECTURE</span></div>
  <div class="card-person">
    <div class="who">DANIEL BRACKWELL</div>
    <div class="role">Director</div>
    <ul>
      <li>03 555 0142 <svg viewBox="0 0 10 10"><path d="M2 1l2 2-1 1.5c.6 1.2 1.3 1.9 2.5 2.5L7 6l2 2-1.5 1.5C4 9 1 6 .5 2.5z"/></svg></li>
      <li>0274 555 019 <svg viewBox="0 0 10 10"><rect x="2.5" y="0.5" width="5" height="9" rx="1"/></svg></li>
      <li>daniel@bsarchitecture.co.nz <svg viewBox="0 0 10 10"><rect x="0.5" y="2" width="9" height="6"/></svg></li>
      <li>PO Box 4180 Fairlie 7925 <svg viewBox="0 0 10 10"><rect x="1" y="3" width="8" height="5"/></svg></li>
      <li>18 Kelvin street Fairlie 7925 <svg viewBox="0 0 10 10"><path d="M5 0a3.5 3.5 0 0 0-3.5 3.5C1.5 6 5 10 5 10s3.5-4 3.5-6.5A3.5 3.5 0 0 0 5 0z"/></svg></li>
    </ul>
  </div>
</section>

</body>
</html>
```